Speisekarten für ein Seerestaurant/Pizzeria
Zielgruppe
Wir sin ein Seerestaurant/Pizzeria in einem Ferien Ort
Aufgabenstellung
Wir brauchen Speisekarte in A4 und A5 Format und wichtig dass wir das Inhalt immer einfach bearbeiten können

```html
<!DOCTYPE html>
<html lang="de">
<head>
<meta charset="utf-8">
<title>Hafenstube – Speisekarte</title>
<link href="https://fonts.googleapis.com/css2?family=Oswald:wght@500;700&family=Abel&family=Jost:wght@300;400&family=Libre+Baskerville&display=swap" rel="stylesheet">
<style>
  :root {
    --bg: #ffffff;
    --paper: #f4f7f8;
    --wash: #6fa3b6;
    --teal: #3f7a90;
    --band: #467b8f;
    --ink: #2c2c2c;
    --text: #5b6468;
    --shell-light: #e8d6bd;
    --shell-dark: #b08a5e;
  }
  * { margin: 0; padding: 0; box-sizing: border-box; }
  html, body { width: 1200px; height: 809px; overflow: hidden; background: var(--bg); }
  .canvas { position: relative; width: 1200px; height: 809px; }

  .page {
    position: absolute; top: 38px; width: 522px; height: 728px; overflow: hidden;
    background: var(--paper);
  }
  .page--cover { left: 43px; }
  .page--menu { left: 629px; }

  .texture {
    position: absolute; inset: 0;
    background:
      linear-gradient(90deg,
        rgba(111,163,182,.05) 0%, rgba(111,163,182,.45) 8%, rgba(111,163,182,.15) 14%,
        rgba(111,163,182,.02) 22%, rgba(111,163,182,.02) 48%, rgba(111,163,182,.3) 53%,
        rgba(111,163,182,.05) 58%, rgba(111,163,182,.02) 82%, rgba(111,163,182,.25) 92%,
        rgba(111,163,182,.05) 100%),
      var(--paper);
  }

  .illustration {
    position: absolute;
    background: radial-gradient(ellipse at 50% 45%, #c9cccd 0%, #e2e4e5 55%, rgba(244,247,248,0) 75%);
  }
  .cover-gull { left: 202px; top: 159px; width: 139px; height: 170px; }
  .menu-gull { left: 37px; top: 21px; width: 86px; height: 103px; }

  .shells {
    position: absolute; left: 0; right: 0; top: 480px; bottom: 0;
    background: linear-gradient(180deg, rgba(232,214,189,0) 0%, var(--shell-light) 14%, #cfae86 55%, var(--shell-dark) 100%);
  }

  .brand-name {
    position: absolute; font-family: "Oswald", sans-serif; font-weight: 500;
    color: var(--ink); line-height: 1; text-align: center; white-space: nowrap;
  }
  .brand-tagline {
    position: absolute; font-family: "Abel", sans-serif; color: var(--ink); text-align: center;
  }
  .page--cover .brand-name { left: 0; right: 0; top: 350px; font-size: 54px; }
  .page--cover .brand-tagline { left: 0; right: 0; top: 420px; font-size: 12px; white-space: nowrap; }
  .page--menu .brand-name { left: 16px; width: 128px; top: 134px; font-size: 25px; }
  .page--menu .brand-tagline { left: 16px; width: 128px; top: 168px; font-size: 7px; line-height: 9px; }

  .section-title {
    position: absolute; left: 143px;
    font-family: "Oswald", sans-serif; font-weight: 700; font-size: 14px;
    letter-spacing: 3.5px; color: var(--teal);
  }

  .dish-list { position: absolute; width: 168px; }
  .dish-list--left { left: 143px; }
  .dish-list--right { left: 320px; }
  .dish { position: relative; height: 24.5px; }
  .dish--tall { height: 32px; }
  .dish-name {
    font-family: "Jost", sans-serif; font-weight: 300; font-size: 7.5px;
    letter-spacing: 2.2px; color: var(--text); line-height: 8px;
  }
  .dish-desc {
    font-family: "Jost", sans-serif; font-weight: 300; font-size: 5.8px;
    color: var(--text); line-height: 7.5px; width: 128px;
  }
  .price {
    position: absolute; right: 0; bottom: 2px;
    font-family: "Libre Baskerville", serif; font-size: 12px; color: var(--teal); line-height: 1;
  }
  .price sup { font-size: 6.5px; vertical-align: 6px; margin-left: 1px; }

  .extras {
    position: absolute; left: 29px; top: 589px; width: 463px; height: 113px;
    background: var(--band); display: flex; padding: 15px 0 0 15px;
  }
  .extras-col { width: 153px; padding-right: 15px; }
  .extras-title {
    font-family: "Oswald", sans-serif; font-weight: 700; font-size: 14px;
    letter-spacing: 3.5px; color: #fff; margin-bottom: 5px; line-height: 16px;
  }
  .extras-row {
    position: relative; height: 17px; display: flex; align-items: center; gap: 6px;
    font-family: "Jost", sans-serif; color: #fff;
  }
  .extras-name { font-weight: 300; font-size: 7.5px; letter-spacing: 2px; }
  .extras-desc { font-weight: 400; font-size: 5.5px; }
  .extras-row .price { color: #fff; bottom: auto; top: 3px; }
</style>
</head>
<body>
<div class="canvas">

  <section class="page page--cover">
    <div class="texture" role="img" aria-label="Weiß gestrichenes Holz mit blauen Farbspuren"></div>
    <div class="illustration cover-gull" role="img" aria-label="Zeichnung einer Möwe auf einem Holzpfahl"></div>
    <h1 class="brand-name">Hafenstube</h1>
    <p class="brand-tagline">Restaurant &amp; Pizzeria an der Seepromenade, Brunndorf</p>
    <div class="shells" role="img" aria-label="Foto von Muscheln und Schneckenhäusern"></div>
  </section>

  <section class="page page--menu">
    <div class="texture" role="img" aria-label="Weiß gestrichenes Holz mit blauen Farbspuren"></div>
    <div class="illustration menu-gull" role="img" aria-label="Zeichnung einer Möwe auf einem Holzpfahl"></div>
    <h1 class="brand-name">Hafenstube</h1>
    <p class="brand-tagline">Restaurant &amp; Pizzeria an der<br>Seepromenade, Brunndorf</p>

    <h2 class="section-title" style="top:48px">STARTERS</h2>
    <div class="dish-list dish-list--left" style="top:99px">
      <div class="dish"><p class="dish-name">Lorem ipsum</p><p class="dish-desc">Lorem ipsum dolor sit amet, consectetuer.</p><span class="price">3<sup>.50</sup></span></div>
      <div class="dish"><p class="dish-name">eros et accumsan</p><p class="dish-desc">Lorem ipsum dolor sit amet, consectetuer.</p><span class="price">5<sup>.20</sup></span></div>
      <div class="dish dish--tall"><p class="dish-name">minim veniam</p><p class="dish-desc">Lorem ipsum dolor sit amet, consectetuer adipiscing elit, sed diam.</p><span class="price">4<sup>.50</sup></span></div>
      <div class="dish dish--tall"><p class="dish-name">vel illum</p><p class="dish-desc">Lorem ipsum dolor sit amet.</p><span class="price">5<sup>.00</sup></span></div>
    </div>
    <div class="dish-list dish-list--right" style="top:99px">
      <div class="dish"><p class="dish-name">Lorem ipsum</p><p class="dish-desc">Lorem ipsum dolor sit amet, consectetuer.</p><span class="price">6<sup>.50</sup></span></div>
      <div class="dish"><p class="dish-name">eros et accumsan</p><p class="dish-desc">Lorem ipsum dolor sit amet, consectetuer.</p><span class="price">2<sup>.50</sup></span></div>
      <div class="dish dish--tall"><p class="dish-name">minim veniam</p><p class="dish-desc">Lorem ipsum dolor sit amet, consectetuer adipiscing elit, sed diam.</p><span class="price">3<sup>.50</sup></span></div>
      <div class="dish dish--tall"><p class="dish-name">vel illum</p><p class="dish-desc">Lorem ipsum dolor sit amet.</p><span class="price">5<sup>.00</sup></span></div>
    </div>

    <h2 class="section-title" style="top:230px">MAIN</h2>
    <div class="dish-list dish-list--left" style="top:281px">
      <div class="dish"><p class="dish-name">Lorem ipsum</p><p class="dish-desc">Lorem ipsum dolor sit amet, consectetuer.</p><span class="price">9<sup>.50</sup></span></div>
      <div class="dish"><p class="dish-name">eros et accumsan</p><p class="dish-desc">Lorem ipsum dolor sit amet, consectetuer.</p><span class="price">5<sup>.50</sup></span></div>
      <div class="dish dish--tall"><p class="dish-name">minim veniam</p><p class="dish-desc">Lorem ipsum dolor sit amet, consectetuer adipiscing elit, sed diam.</p><span class="price">5<sup>.50</sup></span></div>
      <div class="dish dish--tall"><p class="dish-name">vel illum</p><p class="dish-desc">Lorem ipsum dolor sit amet.</p><span class="price">5<sup>.50</sup></span></div>
    </div>
    <div class="dish-list dish-list--right" style="top:281px">
      <div class="dish"><p class="dish-name">Lorem ipsum</p><p class="dish-desc">Lorem ipsum dolor sit amet, consectetuer.</p><span class="price">5<sup>.50</sup></span></div>
      <div class="dish"><p class="dish-name">eros et accumsan</p><p class="dish-desc">Lorem ipsum dolor sit amet, consectetuer.</p><span class="price">5<sup>.50</sup></span></div>
      <div class="dish dish--tall"><p class="dish-name">minim veniam</p><p class="dish-desc">Lorem ipsum dolor sit amet, consectetuer adipiscing elit, sed diam.</p><span class="price">5<sup>.50</sup></span></div>
      <div class="dish dish--tall"><p class="dish-name">vel illum</p><p class="dish-desc">Lorem ipsum dolor sit amet.</p><span class="price">5<sup>.50</sup></span></div>
    </div>

    <h2 class="section-title" style="top:411px">CLASSICS</h2>
    <div class="dish-list dish-list--left" style="top:462px">
      <div class="dish"><p class="dish-name">Lorem ipsum</p><p class="dish-desc">Lorem ipsum dolor sit amet, consectetuer.</p><span class="price">9<sup>.50</sup></span></div>
      <div class="dish"><p class="dish-name">eros et accumsan</p><p class="dish-desc">Lorem ipsum dolor sit amet, consectetuer.</p><span class="price">5<sup>.50</sup></span></div>
      <div class="dish dish--tall"><p class="dish-name">minim veniam</p><p class="dish-desc">Lorem ipsum dolor sit amet, consectetuer adipiscing elit, sed diam.</p><span class="price">5<sup>.50</sup></span></div>
      <div class="dish dish--tall"><p class="dish-name">vel illum</p><p class="dish-desc">Lorem ipsum dolor sit amet.</p><span class="price">5<sup>.50</sup></span></div>
    </div>
    <div class="dish-list dish-list--right" style="top:462px">
      <div class="dish"><p class="dish-name">Lorem ipsum</p><p class="dish-desc">Lorem ipsum dolor sit amet, consectetuer.</p><span class="price">5<sup>.50</sup></span></div>
      <div class="dish"><p class="dish-name">eros et accumsan</p><p class="dish-desc">Lorem ipsum dolor sit amet, consectetuer.</p><span class="price">5<sup>.50</sup></span></div>
      <div class="dish dish--tall"><p class="dish-name">minim veniam</p><p class="dish-desc">Lorem ipsum dolor sit amet, consectetuer adipiscing elit, sed diam.</p><span class="price">5<sup>.50</sup></span></div>
      <div class="dish dish--tall"><p class="dish-name">vel illum</p><p class="dish-desc">Lorem ipsum dolor sit amet.</p><span class="price">5<sup>.50</sup></span></div>
    </div>

    <div class="extras">
      <div class="extras-col">
        <h3 class="extras-title">SIDES</h3>
        <div class="extras-row"><span class="extras-name">Lorem</span><span class="extras-desc">Consectetuert</span><span class="price">5<sup>.50</sup></span></div>
        <div class="extras-row"><span class="extras-name">ipsum</span><span class="extras-desc">Vel illum dolore eu</span><span class="price">5<sup>.50</sup></span></div>
        <div class="extras-row"><span class="extras-name">vel illum</span><span class="extras-desc">Ut wisi enim</span><span class="price">5<sup>.50</sup></span></div>
        <div class="extras-row"><span class="extras-name">sed diam</span><span class="extras-desc">Ullamcorper</span><span class="price">5<sup>.50</sup></span></div>
      </div>
      <div class="extras-col">
        <h3 class="extras-title">DRINKS</h3>
        <div class="extras-row"><span class="extras-name">Lorem</span><span class="extras-desc">Consectetuert</span><span class="price">5<sup>.50</sup></span></div>
        <div class="extras-row"><span class="extras-name">ipsum</span><span class="extras-desc">Vel illum dolore eu</span><span class="price">5<sup>.50</sup></span></div>
        <div class="extras-row"><span class="extras-name">vel illum</span><span class="extras-desc">Ut wisi enim</span><span class="price">5<sup>.50</sup></span></div>
        <div class="extras-row"><span class="extras-name">sed diam</span><span class="extras-desc">Ullamcorper</span><span class="price">5<sup>.50</sup></span></div>
      </div>
      <div class="extras-col">
        <h3 class="extras-title">COFFEE</h3>
        <div class="extras-row"><span class="extras-name">Lorem</span><span class="extras-desc">Consectetuert</span><span class="price">5<sup>.50</sup></span></div>
        <div class="extras-row"><span class="extras-name">ipsum</span><span class="extras-desc">Vel illum dolore eu</span><span class="price">5<sup>.50</sup></span></div>
        <div class="extras-row"><span class="extras-name">vel illum</span><span class="extras-desc">Ut wisi enim</span><span class="price">5<sup>.50</sup></span></div>
        <div class="extras-row"><span class="extras-name">sed diam</span><span class="extras-desc">Ullamcorper</span><span class="price">5<sup>.50</sup></span></div>
      </div>
    </div>
  </section>

</div>
</body>
</html>
```